Get referrals for Insurance customers and the domain name is tallyfinch.ca We are an insurance

We need a logo and a website for a referral site. Our advertising and promotion will send customers to this website where they will fill out a form giving their information as well as person they want to refer. The logo idea that I have is a gear with a dollar sign in it the number 2 and the letter U. Another words dollars to you. If this can be animated with sounds, that would be great. Once this form is filled in it goes to a referral software site such as Lantern Quay or Bonusvale where the data is saved for us to follow up. This is not a complicated site. It will reassure the people who will refer their friends, family members or other aquiatnces that we will provide great service to and best prices for home and business insurance. It will exclude auto insurance as not referral for a monitory reward(regulations). The reward will be $100 for business and house insurance and $25 condo or townhome insurance. It will imply that this $100 is limited time offer. The site should be set so that we could edit the website once the designer has given it to us. The people we expecting to be our referrers are real estate agents, notaries public, and our existing customers.
Updates

The designs are not what I was expecting. Is there any way I can communicate with the designer that I think made the best attempt at what I was expecting?

Target Market(s)

Our customers, realtors, notaries public and anyone who knows

Industry/Entity Type

Insurance Broker

Logo Text

Dollar sign, Gear, number 2 and U a funnel. Dollars to you . See what you can

Number of Pages Required

4 page

Font styles to use
Other font styles liked:
• Calibri

Colors
0455a3
ec1f27
ffffff

Requirements
Must have
• Fillable form on info about referer and the referred. This will data will be sent to the third party who will have our data for keeping track of the referrals and where Our referees can see how many people they have referred and who has been approved for payment. The third parties our such as Lantern Quay or Bonusvale.
Nice to have
• Animated logo with sound would be nice. This will be used on the website only. We use ashgrove insurance logo as seen on www,ashgroveinsurance.ca for all communications.
Should not have
• I have attached two files for reference only they do not have the exact text that I want to have on the website. I am working on that and it will always be changing to some extent. You can talk to me.

```html
<!DOCTYPE html>
<html lang="en">
<head>
<meta charset="utf-8">
<title>Tallyfinch – Get Referrals for Insurance</title>
<link href="https://fonts.googleapis.com/css2?family=Roboto:ital,wght@0,300;0,400;0,500;0,700;1,400&family=Roboto+Condensed:wght@700&display=swap" rel="stylesheet">
<style>
:root{
  --blue:#0455a3;
  --red:#ec1f27;
  --white:#ffffff;
  --ink:#333333;
  --muted:#6b6b6b;
  --line:#cfcfcf;
  --tab:#6d6d6d;
  --soft:#f5f5f5;
}
*{box-sizing:border-box;margin:0;padding:0}
html,body{width:1200px;height:2848px;overflow:hidden;background:var(--white)}
body{position:relative;font-family:'Roboto',sans-serif;color:var(--ink)}
.abs{position:absolute}

/* header */
.site-header{position:absolute;left:0;top:0;width:1200px;height:104px;background:var(--white)}
.brand{position:absolute;left:100px;top:34px;display:flex;align-items:center;gap:12px;font-weight:700;font-size:22px;color:var(--red);letter-spacing:.5px}
.brand-dot{width:34px;height:34px;border:3px solid var(--ink);border-radius:50%}
.nav a{position:absolute;top:46px;font-size:13px;color:var(--ink);text-decoration:none;letter-spacing:.2px}
.nav a.active{color:var(--red)}

/* hero */
.hero{position:absolute;left:0;top:104px;width:1200px;height:700px;overflow:hidden}
.hero-photo{position:absolute;inset:0;background:linear-gradient(100deg,#eef1f4 0%,#e4e9ee 40%,#c9d2db 62%,#b7c3cf 78%,#dbe3ea 100%)}
.hero-curve{position:absolute;left:0;bottom:0}
.slide-arrow{position:absolute;top:270px;width:46px;height:46px;border-radius:50%;background:rgba(255,255,255,.35)}
.form-card{position:absolute;left:101px;top:50px;width:556px;height:540px;background:var(--white);box-shadow:0 2px 10px rgba(0,0,0,.12);border-radius:3px}
.form-card h2{position:absolute;left:30px;top:30px;font-size:18px;font-weight:700;color:#222}
.fieldset{position:absolute;left:32px;width:488px;border:1px solid #ddd;border-radius:2px}
.tab{position:absolute;left:0;top:0;width:150px;height:30px;background:var(--tab);color:var(--white);font-size:14px;line-height:30px;padding-left:22px;border-radius:0 0 12px 0}
.row{position:absolute;left:24px;right:22px;display:flex;align-items:flex-end;gap:8px;font-size:11.5px;color:#333;height:16px}
.fill{flex:1;border-bottom:1px solid var(--line);height:12px}
.opt{display:flex;align-items:center;gap:5px;color:#777;font-size:11px;margin-left:10px}
.box{width:9px;height:9px;border:1px solid #ccc}
.note{position:absolute;left:24px;font-size:10px;color:var(--red)}

/* welcome */
.welcome h1{position:absolute;left:0;width:1200px;top:822px;text-align:center;font-size:38px;font-weight:400;color:var(--blue)}
.welcome p{position:absolute;left:135px;width:930px;text-align:center;font-size:12.5px;line-height:24px;color:var(--muted)}
.btn{position:absolute;left:511px;top:1098px;width:179px;height:40px;background:var(--blue);color:var(--white);font-size:16px;text-align:center;line-height:40px}

/* services */
.services{position:absolute;left:0;top:1225px;width:1200px;height:472px;background:linear-gradient(110deg,#6e7a66 0%,#8a8f86 30%,#7f8fa3 55%,#6f819b 80%,#5e6f86 100%)}
.services h2{position:absolute;left:0;width:1200px;top:58px;text-align:center;font-size:34px;font-weight:300;color:var(--white)}
.svc-mark{position:absolute;top:128px;width:78px;height:78px;border:3px solid var(--white);border-radius:50%}
.svc h3{position:absolute;top:212px;font-family:'Roboto Condensed',sans-serif;font-size:28px;color:var(--white)}
.svc ul{position:absolute;top:262px;list-style:none;color:var(--white);font-size:18px;font-weight:300}
.svc li{height:32px;display:flex;align-items:center;gap:8px}

/* testimonials */
.testimonials{position:absolute;left:0;top:1697px;width:1200px;height:468px;background:var(--soft)}
.testimonials h2{position:absolute;left:0;width:1200px;top:65px;text-align:center;font-size:38px;font-weight:300;color:#333}
.quote{position:absolute;left:208px;top:140px;width:784px;text-align:center;font-size:12.5px;font-style:italic;line-height:22px;color:var(--muted)}
.qmark{position:absolute;font-size:60px;color:#d5d5d5;font-family:Georgia,serif;line-height:1}
.avatar{position:absolute;left:552px;top:233px;width:86px;height:86px;border-radius:50%;border:4px solid var(--white);background:linear-gradient(#cfd3d8,#9aa1a9);box-shadow:0 1px 4px rgba(0,0,0,.15)}
.client-name{position:absolute;left:0;width:1200px;top:335px;text-align:center;font-size:17px;color:var(--red)}
.dots{position:absolute;left:579px;top:385px;display:flex;gap:6px}
.dots i{width:10px;height:10px;border-radius:50%;background:var(--red)}
.dots i.off{background:none;border:2px solid var(--red)}

/* partners */
.partners h2{position:absolute;left:0;width:1200px;top:2222px;text-align:center;font-size:38px;font-weight:300;color:#333}
.partner{position:absolute;top:2320px;width:155px;height:93px;border:1px solid #ddd;display:flex;align-items:center;justify-content:center;font-size:14px;color:#555;font-weight:500;text-align:center}
.chev{position:absolute;top:2352px}

/* footer */
.site-footer{position:absolute;left:0;top:2505px;width:1200px;height:343px;background:var(--blue);color:var(--white)}
.site-footer h4{position:absolute;top:52px;font-size:17px;font-weight:500}
.links a{position:absolute;font-size:13.5px;color:var(--white);text-decoration:none}
.vline{position:absolute;top:50px;width:1px;height:210px;background:rgba(255,255,255,.2)}
.contact{position:absolute;left:487px;font-size:13.5px;line-height:28px}
.email-input{position:absolute;left:777px;top:115px;width:219px;height:38px;background:var(--white);color:#9aa;font-size:13px;line-height:38px;padding-left:14px}
.subscribe{position:absolute;left:996px;top:115px;width:104px;height:38px;background:#1b6dbd;font-size:13.5px;line-height:38px;text-align:center}
.social{position:absolute;top:146px;width:38px;height:38px;border-radius:50%;background:var(--white)}
.footer-rule{position:absolute;left:99px;top:272px;width:1002px;height:1px;background:rgba(255,255,255,.5)}
.copyright{position:absolute;left:99px;top:293px;font-size:13px}
</style>
</head>
<body>

<header class="site-header">
  <div class="brand"><span class="brand-dot"></span>TALLYFINCH</div>
  <nav class="nav">
    <a class="active" style="left:575px">HOME</a>
    <a style="left:663px">ABOUT US</a>
    <a style="left:773px">INSURANCE</a>
    <a style="left:896px">RESOURCES</a>
    <a style="left:1021px">CONTACT US</a>
  </nav>
</header>

<section class="hero">
  <div class="hero-photo" role="img" aria-label="Photo of a smiling senior couple embracing outdoors"></div>
  <div class="slide-arrow" style="left:20px"></div>
  <div class="slide-arrow" style="left:1134px"></div>

  <form class="form-card">
    <h2>Get Referrals for Insurance</h2>

    <div class="fieldset" style="top:80px;height:155px">
      <div class="tab">You</div>
      <div class="row" style="top:50px">Name<span class="fill"></span></div>
      <div class="row" style="top:75px">Agent
        <span class="opt"><span class="box"></span>Sequi Nesciunt</span>
        <span class="opt" style="margin-left:22px"><span class="box"></span>Eius Modi</span>
        <span class="opt" style="margin-left:22px"><span class="box"></span>Voluptate Delit</span></div>
      <div class="row" style="top:100px">Monitory Reward
        <span class="opt"><span class="box"></span>$100 for Business and House</span>
        <span class="opt"><span class="box"></span>$25 Condo or Townhome</span></div>
      <div class="note" style="top:125px">$100 is limited time offer</div>
    </div>

    <div class="fieldset" style="top:258px;height:265px">
      <div class="tab">Your Friend</div>
      <div class="row" style="top:48px">Name<span class="fill"></span></div>
      <div class="row" style="top:74px">Address<span class="fill"></span></div>
      <div class="row" style="top:100px">City<span class="fill" style="flex:0 0 140px"></span><span style="margin-left:22px">State</span><span class="fill" style="flex:0 0 66px"></span><span style="margin-left:16px">Zip</span><span class="fill"></span></div>
      <div class="row" style="top:126px">Telephone<span class="fill" style="flex:0 0 160px"></span><span style="margin-left:12px">Email</span><span class="fill"></span></div>
      <div class="row" style="top:152px">Best time to call
        <span class="opt"><span class="box"></span>A.M.</span>
        <span class="opt"><span class="box"></span>P.M.</span></div>
      <div class="row" style="top:186px">Monitory Reward
        <span class="opt"><span class="box"></span>$100 for Business and House</span>
        <span class="opt"><span class="box"></span>$25 Condo or Townhome</span></div>
      <div class="note" style="top:220px">$100 is limited time offer</div>
    </div>
  </form>

  <svg class="hero-curve" width="1200" height="80" viewBox="0 0 1200 80"><path d="M0,80 L0,45 Q620,-20 1200,40 L1200,80 Z" fill="#ffffff"/></svg>
</section>

<section class="welcome">
  <h1>Welcome to Tallyfinch</h1>
  <p style="top:882px">Sed ut perspiciatis unde omnis iste natus error sit voluptatem accusantium doloremque laudantium, totam rem aperiam, eaque ipsa quae ab illo inventore veritatis et quasi architecto beatae vitae dicta sunt explicabo. Nemo enim ipsam voluptatem quia voluptas sit aspernatur aut odit aut fugit, sed quia consequuntur magni dolores eos qui ratione voluptatem sequi nesciunt.</p>
  <p style="top:972px">Neque porro quisquam est, qui dolorem ipsum quia dolor sit amet, consectetur, adipisci velit, sed quia non numquam eius modi tempora incidunt ut labore et dolore magnam aliquam quaerat voluptatem. Ut enim ad minima veniam, quis nostrum exercitationem ullam corporis suscipit laboriosam, nisi ut aliquid ex ea commodi consequatur? Quis autem vel eum iure reprehenderit qui in ea voluptate velit esse quam nihil molestiae consequatur.</p>
  <div class="btn">LEARN MORE</div>
</section>

<section class="services" role="img" aria-label="Photo of a grey suburban house with autumn trees and a driveway">
  <h2>Our Services</h2>
  <div class="svc">
    <div class="svc-mark" style="left:173px"></div>
    <h3 style="left:99px">HOME INSURANCE</h3>
    <ul style="left:99px">
      <li><svg width="14" height="12" viewBox="0 0 14 12"><path d="M1 6l4 4 8-9" stroke="#fff" stroke-width="2.4" fill="none"/></svg>Single Family homes, Townhouse, Condominiums</li>
      <li><svg width="14" height="12" viewBox="0 0 14 12"><path d="M1 6l4 4 8-9" stroke="#fff" stroke-width="2.4" fill="none"/></svg>Rental/Investment properties</li>
      <li><svg width="14" height="12" viewBox="0 0 14 12"><path d="M1 6l4 4 8-9" stroke="#fff" stroke-width="2.4" fill="none"/></svg>Corporate ownership and/or multiple owners</li>
    </ul>
  </div>
  <div class="svc">
    <div class="svc-mark" style="left:783px"></div>
    <h3 style="left:682px">BUSINESS INSURANCE</h3>
    <ul style="left:682px">
      <li><svg width="14" height="12" viewBox="0 0 14 12"><path d="M1 6l4 4 8-9" stroke="#fff" stroke-width="2.4" fill="none"/></svg>Single Family homes, Townhouse, Condominiums</li>
      <li><svg width="14" height="12" viewBox="0 0 14 12"><path d="M1 6l4 4 8-9" stroke="#fff" stroke-width="2.4" fill="none"/></svg>Rental/Investment properties</li>
      <li><svg width="14" height="12" viewBox="0 0 14 12"><path d="M1 6l4 4 8-9" stroke="#fff" stroke-width="2.4" fill="none"/></svg>Corporate ownership and/or multiple owners</li>
    </ul>
  </div>
</section>

<section class="testimonials">
  <h2>What Client’s Say</h2>
  <span class="qmark" style="left:172px;top:128px">“</span>
  <p class="quote">I am happy to recommend the recruitment service offered by Harbourline Crews. I have recently used the firm’s services and found all staff to be extremely attentive and efficient. They were excessively knowledgeable and approachable at all times, and I would have no hesitation in using their service again.</p>
  <span class="qmark" style="left:975px;top:176px">”</span>
  <div class="avatar" role="img" aria-label="Client portrait photo"></div>
  <div class="client-name">Assumenda Est</div>
  <div class="dots"><i class="off"></i><i></i><i></i></div>
</section>

<section class="partners">
  <h2>Our Client Partners</h2>
  <svg class="chev" style="left:56px" width="16" height="26" viewBox="0 0 16 26"><path d="M13 2L3 13l10 11" stroke="#bbb" stroke-width="3" fill="none"/></svg>
  <div class="partner" style="left:99px">Northbay Group</div>
  <div class="partner" style="left:268px">Elmrow Home</div>
  <div class="partner" style="left:437px">Marrick</div>
  <div class="partner" style="left:606px">Keep Cedarport Green</div>
  <div class="partner" style="left:775px">Reach Onward</div>
  <div class="partner" style="left:944px">Brightvale</div>
  <svg class="chev" style="left:1130px" width="16" height="26" viewBox="0 0 16 26"><path d="M3 2l10 11L3 24" stroke="#bbb" stroke-width="3" fill="none"/></svg>
</section>

<footer class="site-footer">
  <h4 style="left:99px">QUICK LINKS</h4>
  <div class="links">
    <a style="left:99px;top:96px">Home</a>
    <a style="left:99px;top:128px">About us</a>
    <a style="left:99px;top:160px">Insurance</a>
    <a style="left:99px;top:192px">Resources</a>
    <a style="left:280px;top:96px">Terms of Service</a>
    <a style="left:280px;top:128px">Privacy Policy</a>
    <a style="left:280px;top:160px">Contact Us</a>
  </div>
  <div class="vline" style="left:428px"></div>
  <h4 style="left:487px">CONTACT INFO</h4>
  <div class="contact" style="top:88px">Tallyfinch , Street Name, City<br>Address, Country Name, Code.</div>
  <div class="contact" style="top:150px;display:flex;align-items:center;gap:10px"><svg width="13" height="13" viewBox="0 0 24 24"><path d="M6.6 10.8a15 15 0 006.6 6.6l2.2-2.2c.3-.3.7-.4 1-.2 1.1.4 2.3.6 3.6.6.6 0 1 .4 1 1V20c0 .6-.4 1-1 1A17 17 0 013 4c0-.6.4-1 1-1h3.5c.6 0 1 .4 1 1 0 1.3.2 2.5.6 3.6.1.3 0 .7-.2 1z" fill="#fff"/></svg>+00 123 45 67 890</div>
  <div class="contact" style="top:180px;display:flex;align-items:center;gap:10px"><svg width="13" height="11" viewBox="0 0 13 11"><rect width="13" height="11" fill="#fff"/><path d="M0 0l6.5 6L13 0" stroke="#0455a3" stroke-width="1.4" fill="none"/></svg>info@tallyfinch.ca</div>
  <div class="vline" style="left:728px"></div>
  <h4 style="left:774px">SIGN UP FOR NEWSLETTERS</h4>
  <div class="contact" style="left:774px;top:80px;font-size:13px">Please sign up here for latest news</div>
  <div class="email-input">EMAIL ADDRESS</div>
  <div class="subscribe">SUBSCRIBE</div>
  <span class="social" style="left:777px"></span>
  <span class="social" style="left:825px"></span>
  <span class="social" style="left:873px"></span>
  <span class="social" style="left:921px"></span>
  <div class="footer-rule"></div>
  <div class="copyright">© 2017 TALLYFINCH.&nbsp; All right reserved . Term of Use</div>
</footer>

</body>
</html>
```